Settings Menu Design

Need new conceptual designs for App Settings screen. Screen is to be used on Ombrelo device. Simple UX right now is great. Please see rough layouts attached.
Updates

Just want to thank everyone for submitting and working on this. Very appreciative as it's helped push the direction a little further for new revisions.

Target Market(s)

Business owners

Industry/Entity Type

Ombrelo

Font styles to use
Sans Serif

Colors
85cae6
3276b5
33b8a4
fbfbfb
dbdbdb
aaaaaa

Requirements
Must have
• Need new conceptual designs for App Settings screen. App screen will need the following:
• 4 main buttons at the top of the screen. Should include an exit button at the top:
• 1) Main Settings screen - when the user comes to settings home the following are visible: Brightness and Volume need to be interactive to adjust. Battery % needs to be visible. Versioning needs to be visible on-screen as well.
• 2) Network Settings - This has an additional 4 buttons to highlight:
• 1 - A Refresh button. A Column for IP address for a user to interact with and select. Show selected network with an icon. Maybe a star?
• 2 - Wifi Advance - settings to show: Country Code drop down button, SSID section to enter info. Security selection: None, Active. And check box or equivalent to Advanced Options button.
• 3 - Address of device: Ethternet info: _____, Wi-Fi: _____, Tablet: _____
• 4 - QR Code scanner. Tablet will activate front facing the camera and show a live image of what's in front. Needs to read: "Please hold your QR Code in front of me." - Show window of image and section for Country Code drop-down menu.
• 3) Update Applications Section - Showing latest configs and updates with the size of the update. i.e. Prism Loader (0.0.1, 809 mb) - then show item installed, indicated by a checkmark.
• 4) Advanced Settings Screen - Select language ( could be a drop-down menu), Select TimeZone, a button for Usage Feedback, Turn off button, Reboot button, password section that is editable.
• Looking for Clean, flat shaped UI design. Soft drop shadows okay.
• Layout: 1280x800
Should not have
• No beveled or embossed edges. No gloss or glass looking buttons.

```html
<!DOCTYPE html>
<html lang="en">
<head>
<meta charset="UTF-8">
<title>Settings Menu</title>
<link rel="stylesheet" href="https://fonts.googleapis.com/css2?family=Arimo:wght@400;700&family=Roboto+Condensed:wght@400&display=swap">
<style>
  :root {
    --page-bg: #ffffff;
    --dark-header: #3a424a;
    --dark-body: #29333a;
    --dark-divider: #a9a9a9;
    --dark-accent: #1ed8d8;
    --dark-text: #ffffff;
    --dark-muted: #a3a7aa;
    --dark-tab: #b9bcbe;
    --dark-track: #ffffff;
    --dark-knob: #ffffff;

    --light-header: #e1e1e1;
    --light-body: #ebebeb;
    --light-divider: #a0a0a0;
    --light-accent: #85cae6;
    --light-text: #757575;
    --light-muted: #a2a2a2;
    --light-tab: #8d8d8d;
    --light-track: #6c6c6c;
    --light-knob: #6c6c6c;
  }
  * { box-sizing: border-box; margin: 0; padding: 0; }
  html, body { width: 1200px; height: 1000px; overflow: hidden; background: var(--page-bg); }
  .canvas { position: relative; width: 1200px; height: 1000px; overflow: hidden; font-family: "Arimo", Arial, sans-serif; }

  .panel { position: absolute; left: 186px; width: 815px; overflow: hidden; }
  .panel--dark {
    top: 130px; height: 509px;
    --header: var(--dark-header); --body: var(--dark-body); --divider: var(--dark-divider);
    --accent: var(--dark-accent); --text: var(--dark-text); --muted: var(--dark-muted);
    --tab: var(--dark-tab); --track: var(--dark-track); --knob: var(--dark-knob);
  }
  .panel--light {
    top: 660px; height: 340px;
    --header: var(--light-header); --body: var(--light-body); --divider: var(--light-divider);
    --accent: var(--light-accent); --text: var(--light-text); --muted: var(--light-muted);
    --tab: var(--light-tab); --track: var(--light-track); --knob: var(--light-knob);
  }

  .panel__header { position: absolute; left: 0; top: 0; width: 100%; height: 135px; background: var(--header); border-bottom: 3px solid var(--divider); }
  .panel__body { position: absolute; left: 0; top: 135px; width: 100%; bottom: 0; background: var(--body); }

  .tab { position: absolute; top: 32px; width: 76px; height: 76px; border-radius: 50%; border: 3px solid var(--tab); color: var(--tab); display: flex; align-items: center; justify-content: center; }
  .tab svg { width: 44px; height: 44px; }
  .tab--active { border-color: var(--accent); color: var(--accent); }
  .tab--profile { left: 32px; }
  .tab--network { left: 122px; }
  .tab--updates { left: 210px; }
  .tab--advanced { left: 297px; }

  .tab-pointer { position: absolute; left: 55px; top: 118px; width: 0; height: 0; border-left: 13px solid transparent; border-right: 13px solid transparent; border-bottom: 14px solid var(--divider); }

  .close-button { position: absolute; left: 744px; top: 31px; width: 44px; height: 44px; border-radius: 50%; border: 3px solid var(--text); color: var(--text); display: flex; align-items: center; justify-content: center; }
  .panel--light .close-button { border-color: var(--light-track); color: var(--light-track); }
  .close-button svg { width: 20px; height: 20px; }

  .status { position: absolute; top: 102px; font-family: "Roboto Condensed", Arial, sans-serif; font-size: 18px; line-height: 20px; color: var(--muted); }
  .status--battery { left: 528px; }
  .status--version { left: 675px; }

  .settings-title { position: absolute; left: 34px; top: 22px; font-size: 31px; font-weight: 700; color: var(--text); letter-spacing: 0.2px; }

  .setting-row { position: absolute; left: 0; width: 100%; height: 60px; }
  .setting-row--volume { top: 69px; }
  .setting-row--brightness { top: 134px; }
  .panel--light .setting-row { filter: blur(2px); }

  .setting-label { position: absolute; left: 62px; top: 13px; font-size: 27.5px; color: var(--text); }
  .slider { position: absolute; left: 241px; top: 38px; width: 514px; height: 3px; background: var(--track); }
  .slider__fill { position: absolute; left: 0; top: 0; height: 3px; background: var(--accent); }
  .slider__knob { position: absolute; top: -14px; width: 30px; height: 30px; margin-left: -15px; border-radius: 50%; background: var(--knob); }
  .slider__value { position: absolute; top: -34px; width: 60px; margin-left: -28px; text-align: center; font-size: 14px; color: var(--text); }

  .setting-row--volume .slider__fill { width: 317px; }
  .setting-row--volume .slider__knob, .setting-row--volume .slider__value { left: 317px; }
  .setting-row--brightness .slider__fill { width: 462px; }
  .setting-row--brightness .slider__knob, .setting-row--brightness .slider__value { left: 462px; }
</style>
</head>
<body>
<svg width="0" height="0" style="position:absolute">
  <defs>
    <symbol id="icon-sliders" viewBox="0 0 44 44">
      <g fill="none" stroke="currentColor" stroke-width="2.5" stroke-linecap="round">
        <line x1="8" y1="13" x2="36" y2="13"/>
        <line x1="8" y1="22" x2="36" y2="22"/>
        <line x1="8" y1="31" x2="36" y2="31"/>
      </g>
      <g fill="currentColor">
        <circle cx="27" cy="13" r="4"/>
        <circle cx="15" cy="22" r="4"/>
        <circle cx="24" cy="31" r="4"/>
      </g>
    </symbol>
    <symbol id="icon-globe" viewBox="0 0 44 44">
      <g fill="none" stroke="currentColor" stroke-width="2">
        <circle cx="22" cy="22" r="18"/>
        <ellipse cx="22" cy="22" rx="8" ry="18"/>
        <line x1="22" y1="4" x2="22" y2="40"/>
        <line x1="4" y1="22" x2="40" y2="22"/>
        <path d="M7 13 H37 M7 31 H37"/>
      </g>
    </symbol>
    <symbol id="icon-sync" viewBox="0 0 44 44">
      <g fill="currentColor">
        <path d="M6 20 C8 11 18 6 28 10 L31 6 L35 18 L23 18 L26 14 C19 11 12 14 10 20 Z"/>
        <path d="M38 24 C36 33 26 38 16 34 L13 38 L9 26 L21 26 L18 30 C25 33 32 30 34 24 Z"/>
      </g>
    </symbol>
    <symbol id="icon-gear" viewBox="0 0 44 44">
      <circle cx="22" cy="22" r="13" fill="none" stroke="currentColor" stroke-width="7" stroke-dasharray="6.4 3.8"/>
      <circle cx="22" cy="22" r="11.5" fill="currentColor"/>
      <circle cx="22" cy="22" r="5" fill="var(--header)"/>
    </symbol>
    <symbol id="icon-close" viewBox="0 0 20 20">
      <path d="M3 3 L17 17 M17 3 L3 17" stroke="currentColor" stroke-width="2.5" stroke-linecap="round"/>
    </symbol>
  </defs>
</svg>

<main class="canvas">
  <section class="panel panel--dark" aria-label="Settings, dark theme">
    <header class="panel__header">
      <span class="tab tab--profile tab--active"><svg><use href="#icon-sliders"/></svg></span>
      <span class="tab tab--network"><svg><use href="#icon-globe"/></svg></span>
      <span class="tab tab--updates"><svg><use href="#icon-sync"/></svg></span>
      <span class="tab tab--advanced"><svg><use href="#icon-gear"/></svg></span>
      <span class="tab-pointer"></span>
      <span class="close-button"><svg><use href="#icon-close"/></svg></span>
      <span class="status status--battery">BATERRY: 20%</span>
      <span class="status status--version">VERSION: 1.2.3</span>
    </header>
    <div class="panel__body">
      <h2 class="settings-title">MY SETTINGS</h2>
      <div class="setting-row setting-row--volume">
        <span class="setting-label">Volume</span>
        <div class="slider"><span class="slider__fill"></span><span class="slider__value">60%</span><span class="slider__knob"></span></div>
      </div>
      <div class="setting-row setting-row--brightness">
        <span class="setting-label">Brightness</span>
        <div class="slider"><span class="slider__fill"></span><span class="slider__value">90%</span><span class="slider__knob"></span></div>
      </div>
    </div>
  </section>

  <section class="panel panel--light" aria-label="Settings, light theme">
    <header class="panel__header">
      <span class="tab tab--profile tab--active"><svg><use href="#icon-sliders"/></svg></span>
      <span class="tab tab--network"><svg><use href="#icon-globe"/></svg></span>
      <span class="tab tab--updates"><svg><use href="#icon-sync"/></svg></span>
      <span class="tab tab--advanced"><svg><use href="#icon-gear"/></svg></span>
      <span class="tab-pointer"></span>
      <span class="close-button"><svg><use href="#icon-close"/></svg></span>
      <span class="status status--battery">BATERRY: 20%</span>
      <span class="status status--version">VERSION: 1.2.3</span>
    </header>
    <div class="panel__body">
      <h2 class="settings-title">MY SETTINGS</h2>
      <div class="setting-row setting-row--volume">
        <span class="setting-label">Volume</span>
        <div class="slider"><span class="slider__fill"></span><span class="slider__value">60%</span><span class="slider__knob"></span></div>
      </div>
      <div class="setting-row setting-row--brightness">
        <span class="setting-label">Brightness</span>
        <div class="slider"><span class="slider__fill"></span><span class="slider__value">90%</span><span class="slider__knob"></span></div>
      </div>
    </div>
  </section>
</main>
</body>
</html>
```